Lumora Learning Web Design Project

Who We are:
Lumora Learning is education information portal/ magazine, providing information about the Chinese and International education markets. Our aim is to help school principals improve there curriculum, and parents in understanding this curriculum.

Project Brief:
The site will include education news updates, educational services, curriculum developments and overseas study. We hope the site represents the cross cultural bridge between the west and east. The site will cover both the Sciences and Arts.

Note:
The logo design competition is also underway so we only need the website design

What We want:
This competition is for Design only no coding!
Design a home page based on Template 1,2 or 3. I only need to select one.
The design of an article page.

Optional
Design a Microsoft Windows metro style splash page.

Sites We like:
http://www.kavelin.com.cn/kavelinlingo/default.aspx
http://www.brixtalacademia.co.uk/
http://qrpv.norvatestudio.net/

Template Explanations:
Template 1-
The main information has a dynamic sliding category view that when clicked displays the relevant info.
In addition to the main upper menu it also has a left hand sliding menu that pops out on click or gesture

Template 2-
Has limited number of Articles most of the menus are drop downs from the top menu

Template 3-
No Top menu

Target Market(s)

Teachers, principals and parents

Industry/Entity Type

Education

Requirements
Should not have
• kindergarten preschool feel

```html
<!DOCTYPE html>
<html lang="en">
<head>
<meta charset="utf-8">
<title>Lumora Learning</title>
<link href="https://fonts.googleapis.com/css2?family=Raleway:wght@300;400;500;700&display=swap" rel="stylesheet">
<style>
:root{
  --red:#e0413b;
  --red-dark:#c9302b;
  --blue:#1f4f8f;
  --blue-dark:#123e7a;
  --text:#666;
  --text-light:#8a8a8a;
  --line:#e2e2e2;
  --white:#fff;
  --grey-band:#e4e4e4;
}
*{box-sizing:border-box;margin:0;padding:0}
html,body{width:1200px;height:1142px;overflow:hidden}
body{font-family:'Raleway',sans-serif;background:radial-gradient(ellipse at 60% 40%,#f7f7f7 0%,#e6e6e6 70%,#dcdcdc 100%);position:relative;color:var(--text)}
.abs{position:absolute}
.brand{left:168px;top:70px;display:flex;align-items:center;gap:8px}
.brand-dot{width:14px;height:14px;border-radius:50%;background:var(--red)}
.brand-name{font-weight:700;font-size:19px;color:var(--blue)}
.search{left:803px;top:84px;width:221px;height:30px;border:1px solid #fff;background:rgba(255,255,255,.25);display:flex;align-items:center;justify-content:space-between;padding:0 8px 0 10px;font-size:12.5px;color:#fff;letter-spacing:.3px}
.nav{left:166px;top:124px;width:858px;height:41px;background:var(--white);display:flex;box-shadow:0 1px 2px rgba(0,0,0,.08)}
.nav a{display:flex;align-items:center;justify-content:center;padding:0 18px;font-size:13px;color:var(--red);text-decoration:none;border-right:1px solid var(--line)}
.side{left:166px;top:176px;width:65px}
.side-tile{height:66px;display:flex;align-items:center;justify-content:center;background:linear-gradient(#e44a44,#d6352f);border-bottom:1px solid rgba(0,0,0,.06)}
.side-tile.home{background:linear-gradient(#1f5596,#123e7a)}
.social{left:166px;top:648px;width:65px}
.social-tile{height:72px;margin-bottom:5px;background:linear-gradient(#fff,#f2f2f2);display:flex;align-items:center;justify-content:center}
.social-mark{width:18px;height:18px;border-radius:50%;background:#555}
.hero{left:239px;top:176px;width:575px;height:252px;display:flex}
.hero-text{width:260px;background:linear-gradient(#21599a,#133f7c);color:#fff;padding:50px 14px 0}
.hero-title{font-weight:400;font-size:21px;line-height:19px;text-transform:uppercase}
.hero-copy{font-size:11px;line-height:15px;margin-top:12px;font-weight:400}
.more{display:flex;align-items:center;gap:5px;font-size:15px;margin-top:12px;color:#fff}
.hero-photo{flex:1;background:linear-gradient(90deg,#4a4e4c,#6d706e 55%,#c9c3be)}
.cat-head{left:239px;top:438px;width:575px;height:47px}
.panel-head{background:linear-gradient(#e54d47,#d6352f);color:#fff;font-size:24px;font-weight:400;padding-left:14px;display:flex;align-items:center}
.cat-body{left:239px;top:485px;width:575px;height:210px;background:var(--white)}
.card{position:absolute;display:flex;padding:8px;gap:10px;color:#fff}
.card.blue{background:linear-gradient(#21599a,#133f7c)}
.card.red{background:linear-gradient(#e54d47,#d6352f)}
.card-img{width:103px;height:74px;flex:none}
.card h3{font-size:12.5px;font-weight:700;line-height:14.5px;margin-top:2px}
.card .more{font-size:15px;margin-top:4px}
.big-card{position:absolute;left:292px;top:9px;width:275px;height:192px;background:linear-gradient(#e54d47,#d6352f);padding:8px}
.big-card .card-img{width:259px;height:144px}
.big-card h3{color:#fff;font-size:12.5px;font-weight:700;line-height:14.5px;margin-top:7px}
.cat-list{left:239px;top:695px;width:575px}
.cat-row{height:48px;display:flex;align-items:center;background:linear-gradient(#ececec,#dedede);border-bottom:1px solid #f7f7f7;font-size:23px;color:#777;font-weight:400}
.cat-row span{width:278px;padding-left:15px}
.aside{left:823px;width:201px;background:var(--white)}
.aside .panel-head{height:47px}
.aside li{list-style:none;border-bottom:1px solid var(--line);padding:9px 12px;font-size:12.5px;line-height:16px;color:var(--text-light);height:53px}
.foot{left:239px;top:896px;width:785px;height:156px;background:var(--white);display:flex}
.foot-col{border-right:1px solid var(--line);padding:30px 0 0 52px}
.foot-col:last-child{border:none}
.foot-col h4{font-size:15.5px;font-weight:400;color:#555;margin-bottom:5px}
.foot-col a{display:block;font-size:11.5px;line-height:17px;color:var(--text-light);text-decoration:none}
.copy{left:239px;top:1061px;width:785px;height:51px;background:var(--white);display:flex;align-items:center;justify-content:center;font-size:11.5px;color:#999}
.copy b{font-weight:400;color:#666}
</style>
</head>
<body>
<div class="abs brand"><span class="brand-dot"></span><span class="brand-name">LUMORA LEARNING</span></div>
<div class="abs search"><span>SEARCH</span>
<svg width="18" height="18" viewBox="0 0 18 18"><circle cx="7" cy="7" r="5" fill="none" stroke="#fff" stroke-width="2.2"/><line x1="11" y1="11" x2="16" y2="16" stroke="#fff" stroke-width="3" stroke-linecap="round"/></svg></div>

<nav class="abs nav">
<a>HOME</a><a>ABOUT US</a><a>FOR STUDENTS</a><a>LESSON</a><a>BLOG</a><a>JOIN US</a><a>CONTACT</a>
</nav>

<div class="abs side">
<div class="side-tile home"><svg width="24" height="22" viewBox="0 0 24 22"><path d="M12 1 1 11h3v10h6v-6h4v6h6V11h3z" fill="#fff"/></svg></div>
<div class="side-tile"><svg width="24" height="24" viewBox="0 0 24 24"><circle cx="12" cy="12" r="11" fill="#fff"/><text x="12" y="17.5" text-anchor="middle" font-family="Georgia,serif" font-style="italic" font-weight="700" font-size="15" fill="#d6352f">i</text></svg></div>
<div class="side-tile"><svg width="34" height="22" viewBox="0 0 34 22"><path d="M17 2 1 9l16 7 16-7z" fill="#fff"/><path d="M8 13v5c3 3 15 3 18 0v-5l-9 4z" fill="#fff"/><line x1="4" y1="10" x2="4" y2="18" stroke="#fff" stroke-width="1.5"/></svg></div>
<div class="side-tile"><svg width="28" height="20" viewBox="0 0 28 20"><path d="M1 2c5-1 9 0 12 2v15c-3-2-7-3-12-2zM27 2c-5-1-9 0-12 2v15c3-2 7-3 12-2z" fill="#fff"/><g stroke="#d6352f" stroke-width="1"><line x1="4" y1="6" x2="10" y2="7"/><line x1="4" y1="9" x2="10" y2="10"/><line x1="4" y1="12" x2="10" y2="13"/><line x1="18" y1="7" x2="24" y2="6"/><line x1="18" y1="10" x2="24" y2="9"/><line x1="18" y1="13" x2="24" y2="12"/></g></svg></div>
<div class="side-tile"><svg width="18" height="24" viewBox="0 0 18 24"><path d="M1 1h11l5 5v17H1z" fill="#fff"/><g stroke="#d6352f" stroke-width="1.3"><line x1="4" y1="9" x2="14" y2="9"/><line x1="4" y1="12" x2="14" y2="12"/><line x1="4" y1="15" x2="14" y2="15"/><line x1="4" y1="18" x2="14" y2="18"/></g></svg></div>
<div class="side-tile"><svg width="22" height="22" viewBox="0 0 22 22"><g fill="none" stroke="#fff" stroke-width="2.4"><rect x="10" y="2" width="7" height="11" rx="3.5" transform="rotate(40 13.5 7.5)"/><rect x="5" y="9" width="7" height="11" rx="3.5" transform="rotate(40 8.5 14.5)"/></g></svg></div>
<div class="side-tile"><svg width="28" height="20" viewBox="0 0 28 20"><rect x="1" y="1" width="26" height="18" fill="#fff"/><path d="M1 1l13 10L27 1M1 19l9-9M27 19l-9-9" fill="none" stroke="#d6352f" stroke-width="1.2"/></svg></div>
</div>

<div class="abs social">
<div class="social-tile"><span class="social-mark"></span></div>
<div class="social-tile"><span class="social-mark"></span></div>
<div class="social-tile"><span class="social-mark"></span></div>
<div class="social-tile"><span class="social-mark"></span></div>
<div class="social-tile"><span class="social-mark"></span></div>
<div class="social-tile"><svg width="20" height="20" viewBox="0 0 20 20"><circle cx="3" cy="17" r="2.6" fill="#555"/><path d="M1 8a11 11 0 0 1 11 11M1 2a17 17 0 0 1 17 17" fill="none" stroke="#555" stroke-width="3"/></svg></div>
</div>

<section class="abs hero">
<div class="hero-text">
<h1 class="hero-title">Raising the skill levels of students in home convenience</h1>
<p class="hero-copy">Lorem ipsum dolor sit amet, consectetuer adipiscing elit, sed diam nonummy nibh euismod tincidunt ut.</p>
<div class="more"><svg width="17" height="12" viewBox="0 0 17 12"><path d="M1 1l5 5-5 5M9 1l5 5-5 5" fill="none" stroke="#fff" stroke-width="2.4"/></svg>read more</div>
</div>
<div class="hero-photo" role="img" aria-label="Teacher in a white coat smiling in front of a chalkboard with science formulas"></div>
</section>

<div class="abs cat-head panel-head">CATEGORIES</div>
<section class="abs cat-body">
<div class="card blue" style="left:9px;top:9px;width:274px;height:92px">
<div class="card-img" role="img" aria-label="Classroom of students raising their hands" style="background:linear-gradient(#34404a,#6a5a52)"></div>
<div><h3>Lorem ipsum dolor sit amet, consectetuer adipiscing elit.</h3>
<div class="more"><svg width="17" height="12" viewBox="0 0 17 12"><path d="M1 1l5 5-5 5M9 1l5 5-5 5" fill="none" stroke="#fff" stroke-width="2.4"/></svg>read more</div></div>
</div>
<div class="card red" style="left:9px;top:110px;width:274px;height:92px">
<div class="card-img" role="img" aria-label="Student working at a computer in a lab" style="background:linear-gradient(90deg,#dfe3e6,#8a7a6c 70%,#9cc06a)"></div>
<div><h3>Lorem ipsum dolor sit amet, consectetuer adipiscing elit.</h3>
<div class="more"><svg width="17" height="12" viewBox="0 0 17 12"><path d="M1 1l5 5-5 5M9 1l5 5-5 5" fill="none" stroke="#fff" stroke-width="2.4"/></svg>read more</div></div>
</div>
<div class="big-card">
<div class="card-img" role="img" aria-label="Teacher helping a group of young pupils drawing at a desk" style="background:linear-gradient(135deg,#c9a47a,#e8c48e 45%,#b98a5a)"></div>
<h3>Lorem ipsum dolor sit amet, consectetuer adipiscing elit.</h3>
</div>
</section>

<div class="abs cat-list">
<div class="cat-row"><span>EUROPE</span><span>DRAMA</span></div>
<div class="cat-row"><span>ASIA</span><span>SCIENCE</span></div>
<div class="cat-row"><span>USA</span><span>ENGLISH</span></div>
<div class="cat-row"><span>AUSTRALIA</span><span>ARTS</span></div>
</div>

<aside class="abs aside" style="top:176px;height:363px">
<div class="panel-head">ARTICLES</div>
<ul>
<li>Ut viverra nibh sit amet eros luctus convallis.</li>
<li>Phasellus et libero at leo molestie dapibus.</li>
<li>Ut viverra nibh sit amet eros luctus convallis.</li>
<li>Suspendisse dignissim sapien hendrerit mi</li>
<li>Pellentesque, convallis tincidunt justo auctor.</li>
<li>Proin ut ligula egestas, tempus dui vel, sollicitudin leo.</li>
</ul>
</aside>

<aside class="abs aside" style="top:549px;height:338px">
<div class="panel-head">BLOG POSTS</div>
<ul>
<li>Ut viverra nibh sit amet eros luctus convallis.</li>
<li>Phasellus et libero at leo molestie dapibus.</li>
<li>Ut viverra nibh sit amet eros luctus convallis.</li>
<li>Suspendisse dignissim sapien hendrerit mi</li>
<li>Pellentesque, convallis tincidunt justo auctor.</li>
</ul>
</aside>

<footer class="abs foot">
<div class="foot-col" style="width:167px"><h4>Quick Links</h4><a>Home</a><a>About Us</a><a>Support</a><a>Team</a><a>Contact Us</a></div>
<div class="foot-col" style="width:190px;padding-left:65px"><h4>Education</h4><a>Syllabus</a><a>Submit a Content</a><a>Consulting</a><a>Programs</a></div>
<div class="foot-col" style="width:189px"><h4>Quick Links</h4><a>Home</a><a>About Us</a><a>Support</a><a>Team</a><a>Contact Us</a></div>
<div class="foot-col" style="width:239px;padding-left:45px"><h4>Education</h4><a>Syllabus</a><a>Submit a Content</a><a>Consulting</a><a>Programs</a></div>
</footer>

<div class="abs copy">Copyright © 2013 LumoraLearning.&nbsp;<b>All rights reserved</b></div>
</body>
</html>
```